Design 5 colour schemes for one web page

We are looking for 5 different colour schemes for our product template to create different kinds of colour tone for our web page, it doesn't need to be restructure the layout, just need to provide different color solution.

Please refer to the attached images and take note of the following when you’re working on the design:
(1) Please precisely reproduce the layout. Cannot remove or delete any wordings, components or column shown in the images.
(2) Okay to revise icons, background color or text style as you prefer. But cannot move/delete them.
(3) Provide PSD source files with good layer management. HTML/CSS are not required.
(4) Make reasonable and professional design.

After completion, please send back:
(1) 5 images with 5 different colour schemes.
(2) Related PSD files.

Font styles to use
Serif
Sans Serif

Requirements
Must have
• (1) 5 images for the colour schemes.
• (2) 5 PSD source files with good layer management.
Nice to have
• (1) Explanation about your design of the colour schemes.
Should not have
• (1) HTML/CSS code are not required.

```html
<!DOCTYPE html>
<html lang="en">
<head>
<meta charset="utf-8">
<title>Sports</title>
<link href="https://fonts.googleapis.com/css2?family=Open+Sans:wght@400;600;700&display=swap" rel="stylesheet">
<style>
:root{
  --topbar:#1d2231;
  --topbar-dark:#151925;
  --accent:#f0892a;
  --accent-dark:#d8741b;
  --side:#272d3e;
  --side-dark:#1f2433;
  --side-tab:#343b50;
  --side-text:#c4c9d6;
  --bg-top:#efe8df;
  --bg-mid:#cdb8a0;
  --bg-bot:#8a6e55;
  --head-light:#f6f4f1;
  --head-col:#ebe7e2;
  --league:#e4dfd8;
  --line:#ddd8d1;
  --text:#33384a;
  --muted:#8e909a;
  --away:#d0392b;
  --ou:#e07a1a;
  --bet:#2fae93;
  --badge-dark:#141824;
}
*{box-sizing:border-box;margin:0;padding:0}
html,body{width:864px;height:1200px;overflow:hidden}
body{font-family:"Open Sans",sans-serif;color:var(--text);background:linear-gradient(180deg,var(--bg-top) 0%,var(--bg-mid) 60%,var(--bg-bot) 100%);position:relative;font-size:8px}
.abs{position:absolute}
.topbar{left:0;top:0;width:864px;height:30px;background:var(--topbar);color:#fff}
.topbar span{position:absolute;top:10px;font-size:8px}
.badge{background:var(--away);color:#fff;padding:1px 4px;font-size:6.5px;font-weight:400}
.wallet{left:654px;top:0;width:101px;height:30px;background:var(--topbar-dark);color:#fff;font-size:8px;padding:10px 0 0 7px;white-space:nowrap}
.signout{left:755px;top:0;width:51px;height:30px;background:var(--accent);color:#fff;text-align:center;line-height:30px;font-size:8px}
.header{left:58px;top:52px;width:748px;height:62px;background:var(--accent);color:#fff}
.logo{position:absolute;left:10px;top:13px;font-size:29px;font-weight:600;letter-spacing:.5px;line-height:1.2}
.nav{position:absolute;top:32px;font-size:8px;font-weight:600}
.nav.on{color:var(--topbar)}
.new{position:absolute;left:412px;top:8px;background:var(--away);font-size:6.5px;padding:2px 6px}
.util{position:absolute;top:25px;font-size:7.5px}
.subbar{left:58px;top:114px;width:748px;height:26px;background:var(--accent-dark);color:#fff;font-size:7.5px}
.subbar .t{position:absolute;top:8px}
.tool{position:absolute;top:0;height:26px;border-left:1px solid rgba(255,255,255,.25);width:31px;text-align:center;line-height:26px;font-size:7.5px}
.live-btn{position:absolute;left:706px;top:5px;width:31px;height:16px;background:var(--badge-dark);color:#fff;text-align:center;line-height:16px;font-size:6.5px}
.sidebar{left:58px;top:140px;width:150px;height:687px;background:var(--side);color:var(--side-text)}
.side-head{height:35px;background:var(--side-dark);color:#fff;font-size:7.5px;font-weight:600;padding:12px 11px}
.side-note{height:47px;padding:8px 11px;font-size:7.5px;line-height:1.5}
.tabs{display:flex;height:29px;background:var(--side-dark);font-size:7.5px;font-weight:600;color:#fff}
.tabs div{flex:1;padding:10px 11px}
.tabs .on{background:var(--side-tab)}
.sports{list-style:none;padding-top:6px}
.sports li{height:20.8px;display:flex;align-items:center;padding:0 11px;font-size:7.8px}
.sports li i{width:11px;height:11px;border-radius:50%;border:1.5px solid #d7dbe4;margin-right:10px}
.sports li b{margin-left:auto;background:var(--badge-dark);color:#fff;font-size:5.5px;font-weight:400;padding:2px 4px}
.ticket{position:absolute;top:534px;left:0;width:150px;height:26px;display:flex;font-size:7.5px;color:#fff}
.ticket div{flex:1;text-align:center;line-height:26px;background:var(--side-dark)}
.ticket .parlay{background:var(--accent)}
.ticket .parlay em{font-style:normal;background:var(--badge-dark);padding:2px 3px;margin-left:4px}
.mybets{position:absolute;top:560px;left:0;width:150px;height:28px;background:var(--side-dark);color:#fff;font-size:7.5px;font-weight:600;padding:10px 11px}
.refresh{position:absolute;top:588px;left:0;width:150px;height:29px;padding:10px 11px;font-size:7.5px;color:#fff;background:var(--side-dark)}
.pending{position:absolute;top:617px;left:0;padding:10px 11px;font-size:7.5px}
.viewall{position:absolute;top:656px;left:11px;width:127px;height:22px;background:var(--accent);color:#fff;text-align:center;line-height:22px;font-size:7.5px}
.main{left:208px;top:140px;width:598px;height:961px;background:#fff}
.sec-head{height:36px;display:flex;align-items:center;padding:0 14px;font-size:7.5px;background:var(--head-light);position:relative}
.sec-head.dark{background:var(--side);color:#fff}
.sec-head .runner{width:8px;height:14px;border-left:2px solid currentColor;transform:skew(-20deg);margin-right:10px}
.sec-head .count{position:absolute;left:300px;font-size:9px;font-weight:600}
.sec-head .league-sel{margin-left:auto;font-size:7.5px}
.grid{display:grid;grid-template-columns:50px 142px repeat(8,43px) 62px}
.colhead{height:48px;background:var(--head-col);color:#555a66;font-size:7.5px}
.colhead .span{grid-row:1/3;display:flex;align-items:center;justify-content:center;border-right:1px solid #fff}
.colhead .grp{grid-column:span 4;display:flex;align-items:center;justify-content:center;height:24px;border-right:1px solid #fff;border-bottom:1px solid #fff}
.colhead .sub{height:24px;display:flex;align-items:center;justify-content:center;color:var(--muted);border-right:1px solid #fff}
.league{height:31px;background:var(--league);display:flex;align-items:center;position:relative;font-size:6.8px}
.league.light{background:var(--head-light)}
.league.hl{background:var(--accent);color:#fff}
.league .nm{position:absolute;left:70px;display:flex;align-items:center}
.league .nm:before{content:"★";font-size:8px;margin-right:6px}
.league .ref{position:absolute;right:16px;width:8px;height:8px;border:1.3px solid currentColor;border-radius:50%;border-top-color:transparent}
.match{height:46px;border-bottom:1px solid var(--line);font-size:7.5px}
.match>div{height:45px;display:flex;align-items:center}
.match>.c-time,.match>.c-ev,.match>.f4{border-right:1px solid var(--line)}
.c-time{padding-left:4px;gap:9px}
.c-time .ic{width:7px;height:7px;background:#6b6f7a}
.c-time .tm{line-height:1.4;font-size:7px}
.live{color:var(--away)}
.c-ev{gap:9px;padding-left:5px;line-height:1.25}
.c-ev .st{color:#f1b520;font-size:10px}
.away{color:var(--away)}
.c{justify-content:center}
.odds{flex-direction:column;line-height:1.9}
.ou{color:var(--ou)}
.ou-cell{gap:14px}
.ou-cell .ou-l{line-height:1.9;text-align:center;font-size:7px}
.bet{background:var(--bet);color:#fff;font-size:8.5px;padding:3px 6px;white-space:nowrap}
.bet:before{content:"↕ ";font-size:7px}
.footer{left:0;top:1122px;width:864px;text-align:center;color:#fff;font-size:8px;line-height:2}
.footer .sep{margin:0 9px}
.social{position:absolute;top:1164px;width:21px;height:21px;border:1.3px solid #fff;border-radius:50%}
</style>
</head>
<body>
<div class="abs topbar">
  <span style="left:57px">My Bets</span>
  <span style="left:108px">Statement</span>
  <span style="left:169px">Balance</span>
  <span style="left:220px">Account</span>
  <span style="left:272px">Announcements <b class="badge">99+</b></span>
  <span style="left:598px">Hi, Player042</span>
</div>
<div class="abs wallet">»&nbsp; SD$ &nbsp;10,072.00 ↻</div>
<div class="abs signout">SIGN OUT</div>

<div class="abs header">
  <div class="logo">SPORTS</div>
  <span class="nav" style="left:186px">HOME</span>
  <span class="nav on" style="left:240px">SPORTS</span>
  <span class="nav" style="left:299px">LIVE SPORTS</span>
  <span class="nav" style="left:371px">LIVE CASINO</span>
  <span class="new">NEW</span>
  <span class="util" style="left:611px">● Results</span>
  <span class="util" style="left:656px">● Live Chat</span>
  <span class="util" style="left:710px">● Help</span>
</div>

<div class="abs subbar">
  <span class="t" style="left:12px">◉ &nbsp;&nbsp;English (Asia) ▾</span>
  <span class="t" style="left:109px">12/02/2014 15:53PM GMT+8</span>
  <div class="tool" style="left:517px;width:36px">⊕ ▾</div>
  <div class="tool" style="left:553px">★ ▾</div>
  <div class="tool" style="left:584px">● ▾</div>
  <div class="tool" style="left:615px">MY ▾</div>
  <div class="tool" style="left:646px">◁)</div>
  <div class="tool" style="left:677px">▣</div>
  <div class="live-btn">LIVE</div>
</div>

<div class="abs sidebar">
  <div class="side-head">MY FAVOURITES</div>
  <div class="side-note">Click o an event or league to add to “My favourites”</div>
  <div class="tabs"><div class="on">SPORTS</div><div>MARKETS</div></div>
  <ul class="sports">
    <li><i></i>Football<b>600</b></li>
    <li><i></i>Basketball<b>600</b></li>
    <li><i></i>Baseball<b>600</b></li>
    <li><i></i>Tennis<b>600</b></li>
    <li><i></i>American Football<b>600</b></li>
    <li><i></i>Badminton<b>600</b></li>
    <li><i></i>Boxing<b>600</b></li>
    <li><i></i>Cricket<b>600</b></li>
    <li><i></i>Cycling<b>600</b></li>
    <li><i></i>Darts<b>600</b></li>
    <li><i></i>Entertainment<b>600</b></li>
    <li><i></i>Golf<b>600</b></li>
    <li><i></i>Handball<b>600</b></li>
    <li><i></i>Ice Hockey<b>600</b></li>
    <li><i></i>Mixed martial Arts<b>600</b></li>
    <li><i></i>Miotor Sport<b>600</b></li>
    <li><i></i>Pool/Snooker<b>600</b></li>
    <li><i></i>Rugby<b>600</b></li>
    <li><i></i>Volleyball<b>600</b></li>
    <li><i></i>Winter Sports<b>600</b></li>
  </ul>
  <div class="ticket"><div>TICKET</div><div class="parlay">PARLAY<em>0</em></div></div>
  <div class="mybets">MY BETS</div>
  <div class="refresh">↻ Refresh</div>
  <div class="pending">No Pending Bets</div>
  <div class="viewall">VIEW ALL</div>
</div>

<div class="abs main">
  <div class="sec-head"><span class="runner"></span>TODAY LIVE<span class="count">↻ 38</span><span class="league-sel">🏆 SELECT LEAGUE</span></div>
  <div class="grid colhead">
    <div class="span">TIME</div><div class="span">EVENT</div>
    <div class="grp">FULL TIME</div><div class="grp">FIRST HALF</div>
    <div class="span" style="grid-column:11;grid-row:1/3">+ MORE</div>
    <div class="sub">A1X2</div><div class="sub">HDP</div><div class="sub">OU</div><div class="sub">1X2</div>
    <div class="sub">A1X2</div><div class="sub">HDP</div><div class="sub">OU</div><div class="sub">1X2</div>
  </div>
  <div class="league hl"><span class="nm">Coastal Premier League</span><span class="ref"></span></div>
  <div class="grid match"><div class="c-time"><span class="ic"></span><span class="tm">16:30<br><span class="live">Live</span></span></div><div class="c-ev"><span class="st">☆</span><span>Eastshore Mariners<br><span class="away">Southport Rovers</span></span></div><div class="c">0-0.5</div><div class="c odds"><span>0.77</span><span class="away">-0.95</span></div><div class="c ou-cell"><span class="ou">6-6.5</span><span class="ou-l">o<br>u</span></div><div class="c odds f4"><span>0.77</span><span class="away">-0.95</span></div><div></div><div></div><div></div><div></div><div class="c"><span class="bet">13</span></div></div>

  <div class="sec-head dark"><span class="runner"></span>TODAY NON LIVE<span class="count">↻ 38</span><span class="league-sel">🏆 SELECT LEAGUE</span></div>
  <div class="grid colhead">
    <div class="span">TIME</div><div class="span">EVENT</div>
    <div class="grp">FULL TIME</div><div class="grp">FIRST HALF</div>
    <div class="span" style="grid-column:11;grid-row:1/3">+ MORE</div>
    <div class="sub">A1X2</div><div class="sub">HDP</div><div class="sub">OU</div><div class="sub">1X2</div>
    <div class="sub">A1X2</div><div class="sub">HDP</div><div class="sub">OU</div><div class="sub">1X2</div>
  </div>

  <div class="league light"><span class="nm">Coastal Premier League</span><span class="ref"></span></div>
  <div class="grid match"><div class="c-time"><span class="ic"></span><span class="tm">16:30<br><span class="live">Live</span></span></div><div class="c-ev"><span class="st">☆</span><span>Eastshore Mariners<br><span class="away">Southport Rovers</span></span></div><div class="c">0-0.5</div><div class="c odds"><span>0.77</span><span class="away">-0.95</span></div><div class="c ou-cell"><span class="ou">6-6.5</span><span class="ou-l">o<br>u</span></div><div class="c odds f4"><span>0.77</span><span class="away">-0.95</span></div><div></div><div></div><div></div><div></div><div class="c"><span class="bet">13</span></div></div>

  <div class="league"><span class="nm">Coastal Premier League</span><span class="ref"></span></div>
  <div class="grid match"><div class="c-time"><span class="ic"></span><span class="tm">16:30<br><span class="live">Live</span></span></div><div class="c-ev"><span class="st">☆</span><span>Eastshore Mariners<br><span class="away">Southport Rovers</span></span></div><div class="c">0-0.5</div><div class="c odds"><span>0.77</span><span class="away">-0.95</span></div><div class="c ou-cell"><span class="ou">6-6.5</span><span class="ou-l">o<br>u</span></div><div class="c odds f4"><span>0.77</span><span class="away">-0.95</span></div><div></div><div></div><div></div><div></div><div class="c"><span class="bet">13</span></div></div>
  <div class="grid match"><div class="c-time"><span class="ic"></span><span class="tm">16:30<br><span class="live">Live</span></span></div><div class="c-ev"><span class="st">☆</span><span>Eastshore Mariners<br><span class="away">Southport Rovers</span></span></div><div class="c">0-0.5</div><div class="c odds"><span>0.77</span><span class="away">-0.95</span></div><div class="c ou-cell"><span class="ou">6-6.5</span><span class="ou-l">o<br>u</span></div><div class="c odds f4"><span>0.77</span><span class="away">-0.95</span></div><div></div><div></div><div></div><div></div><div class="c"><span class="bet">13</span></div></div>
  <div class="grid match"><div class="c-time"><span class="ic"></span><span class="tm">16:30<br><span class="live">Live</span></span></div><div class="c-ev"><span class="st">☆</span><span>Eastshore Mariners<br><span class="away">Southport Rovers</span></span></div><div class="c">0-0.5</div><div class="c odds"><span>0.77</span><span class="away">-0.95</span></div><div class="c ou-cell"><span class="ou">6-6.5</span><span class="ou-l">o<br>u</span></div><div class="c odds f4"><span>0.77</span><span class="away">-0.95</span></div><div></div><div></div><div></div><div></div><div class="c"><span class="bet">13</span></div></div>

  <div class="league"><span class="nm">Coastal Premier League</span><span class="ref"></span></div>
  <div class="grid match"><div class="c-time"><span class="ic"></span><span class="tm">16:30<br><span class="live">Live</span></span></div><div class="c-ev"><span class="st">☆</span><span>Eastshore Mariners<br><span class="away">Southport Rovers</span></span></div><div class="c">0-0.5</div><div class="c odds"><span>0.77</span><span class="away">-0.95</span></div><div class="c ou-cell"><span class="ou">6-6.5</span><span class="ou-l">o<br>u</span></div><div class="c odds f4"><span>0.77</span><span class="away">-0.95</span></div><div></div><div></div><div></div><div></div><div class="c"><span class="bet">13</span></div></div>

  <div class="league"><span class="nm">Coastal Premier League</span><span class="ref"></span></div>
  <div class="grid match"><div class="c-time"><span class="ic"></span><span class="tm">16:30<br><span class="live">Live</span></span></div><div class="c-ev"><span class="st">☆</span><span>Eastshore Mariners<br><span class="away">Southport Rovers</span></span></div><div class="c">0-0.5</div><div class="c odds"><span>0.77</span><span class="away">-0.95</span></div><div class="c ou-cell"><span class="ou">6-6.5</span><span class="ou-l">o<br>u</span></div><div class="c odds f4"><span>0.77</span><span class="away">-0.95</span></div><div></div><div></div><div></div><div></div><div class="c"><span class="bet">13</span></div></div>
  <div class="grid match"><div class="c-time"><span class="ic"></span><span class="tm">16:30<br><span class="live">Live</span></span></div><div class="c-ev"><span class="st">☆</span><span>Eastshore Mariners<br><span class="away">Southport Rovers</span></span></div><div class="c">0-0.5</div><div class="c odds"><span>0.77</span><span class="away">-0.95</span></div><div class="c ou-cell"><span class="ou">6-6.5</span><span class="ou-l">o<br>u</span></div><div class="c odds f4"><span>0.77</span><span class="away">-0.95</span></div><div></div><div></div><div></div><div></div><div class="c"><span class="bet">13</span></div></div>
  <div class="grid match"><div class="c-time"><span class="ic"></span><span class="tm">16:30<br><span class="live">Live</span></span></div><div class="c-ev"><span class="st">☆</span><span>Eastshore Mariners<br><span class="away">Southport Rovers</span></span></div><div class="c">0-0.5</div><div class="c odds"><span>0.77</span><span class="away">-0.95</span></div><div class="c ou-cell"><span class="ou">6-6.5</span><span class="ou-l">o<br>u</span></div><div class="c odds f4"><span>0.77</span><span class="away">-0.95</span></div><div></div><div></div><div></div><div></div><div class="c"><span class="bet">13</span></div></div>
  <div class="grid match"><div class="c-time"><span class="ic"></span><span class="tm">16:30<br><span class="live">Live</span></span></div><div class="c-ev"><span class="st">☆</span><span>Eastshore Mariners<br><span class="away">Southport Rovers</span></span></div><div class="c">0-0.5</div><div class="c odds"><span>0.77</span><span class="away">-0.95</span></div><div class="c ou-cell"><span class="ou">6-6.5</span><span class="ou-l">o<br>u</span></div><div class="c odds f4"><span>0.77</span><span class="away">-0.95</span></div><div></div><div></div><div></div><div></div><div class="c"><span class="bet">13</span></div></div>
  <div class="grid match"><div class="c-time"><span class="ic"></span><span class="tm">16:30<br><span class="live">Live</span></span></div><div class="c-ev"><span class="st">☆</span><span>Eastshore Mariners<br><span class="away">Southport Rovers</span></span></div><div class="c">0-0.5</div><div class="c odds"><span>0.77</span><span class="away">-0.95</span></div><div class="c ou-cell"><span class="ou">6-6.5</span><span class="ou-l">o<br>u</span></div><div class="c odds f4"><span>0.77</span><span class="away">-0.95</span></div><div></div><div></div><div></div><div></div><div class="c"><span class="bet">13</span></div></div>
  <div class="grid match"><div class="c-time"><span class="ic"></span><span class="tm">16:30<br><span class="live">Live</span></span></div><div class="c-ev"><span class="st">☆</span><span>Eastshore Mariners<br><span class="away">Southport Rovers</span></span></div><div class="c">0-0.5</div><div class="c odds"><span>0.77</span><span class="away">-0.95</span></div><div class="c ou-cell"><span class="ou">6-6.5</span><span class="ou-l">o<br>u</span></div><div class="c odds f4"><span>0.77</span><span class="away">-0.95</span></div><div></div><div></div><div></div><div></div><div class="c"><span class="bet">13</span></div></div>
  <div class="grid match"><div class="c-time"><span class="ic"></span><span class="tm">16:30<br><span class="live">Live</span></span></div><div class="c-ev"><span class="st">☆</span><span>Eastshore Mariners<br><span class="away">Southport Rovers</span></span></div><div class="c">0-0.5</div><div class="c odds"><span>0.77</span><span class="away">-0.95</span></div><div class="c ou-cell"><span class="ou">6-6.5</span><span class="ou-l">o<br>u</span></div><div class="c odds f4"><span>0.77</span><span class="away">-0.95</span></div><div></div><div></div><div></div><div></div><div class="c"><span class="bet">13</span></div></div>
</div>

<div class="abs footer">
  <div>Batting Rates<span class="sep">|</span>Contac us<span class="sep">|</span>Privacy Policy<span class="sep">|</span>Responsible Gambling</div>
  <div style="font-size:7.5px">Terms and Conditions<span class="sep">|</span>Tutorials<span class="sep">|</span><span style="font-size:6.5px">© 2014 All rights reserved</span></div>
</div>
<span class="social" style="left:393px"></span>
<span class="social" style="left:422px"></span>
<span class="social" style="left:451px"></span>
</body>
</html>
```